依頼詳細
会社の新しいロゴを添付します。
・MOON.K.ランド株式会社
・ロゴの色とマッチする名刺デザインでお願いします。
記載項目
■ロゴ
■企業情報
会社名/住所/電話番号/FAX番号/URL
■個人の情報
氏名/氏名のローマ字表記/役職/電話番号/メールアドレス
希望イメージ
シンプル 複雑
単色 カラフル
暗い 明るい
日常 高級
遊び心 厳粛
未来的 伝統的
女性的 男性的
希望する色
納品ファイル
• 高解像度JPG (.jpg)
• イラストレーター形式 (.ai)
• PNG形式 (.png)
補足説明

当方の想定していたイメージに最も合ったデザインを作成いただけました。
また機会があればお願いさせていただきたいです。

この度はご提案いただきありがとうございました。
当方の想定していたイメージに最も合ったデザインを作成いただけましたので、こちらを採用させていただきました。
今後も機会がありましたらよろしくお願いいたします。
ありがとうございました。

```html
<!DOCTYPE html>
<html lang="ja">
<head>
<meta charset="UTF-8">
<title>HARUNA SYSTEMS 名刺デザイン</title>
<link href="https://fonts.googleapis.com/css2?family=Noto+Sans+JP:wght@400;500;700&display=swap" rel="stylesheet">
<style>
  :root {
    --page-bg: #ffffff;
    --card-white: #ffffff;
    --brand-navy: #1f45a3;
    --brand-blue: #2a6fc4;
    --brand-sky: #35a6e6;
    --text-main: #2b3f86;
    --text-sub: #4a5b8f;
    --text-white: #ffffff;
  }
  * { box-sizing: border-box; margin: 0; padding: 0; }
  html, body {
    width: 900px; height: 1200px; overflow: hidden;
    background: var(--page-bg);
    font-family: "Noto Sans JP", sans-serif;
  }
  .sheet { position: relative; width: 900px; height: 1200px; }
  .card {
    position: absolute; left: 84px; width: 732px; height: 440px;
    box-shadow: 0 2px 8px rgba(0,0,0,0.18);
    overflow: hidden;
  }
  .card--front { top: 66px; background: var(--card-white); }
  .card--back { top: 684px; background: var(--brand-navy); }

  .symbol-area {
    position: absolute; left: 420px; top: -40px; width: 270px; height: 270px;
    border-radius: 50%;
    background: linear-gradient(135deg, var(--brand-sky) 0%, var(--brand-blue) 55%, var(--brand-navy) 100%);
  }

  .person { position: absolute; left: 36px; top: 104px; color: var(--text-main); }
  .person__name { font-size: 22px; font-weight: 500; letter-spacing: 1px; }
  .person__roman { font-size: 13px; font-weight: 400; margin-left: 10px; letter-spacing: 1px; }
  .person__title { font-size: 13px; margin-top: 2px; letter-spacing: 2px; }

  .contact { position: absolute; left: 36px; top: 172px; color: var(--text-sub); font-size: 12px; }
  .contact__row { display: flex; align-items: center; gap: 8px; height: 30px; }
  .contact__icon { width: 13px; height: 13px; fill: var(--text-main); }

  .company-mark { display: flex; align-items: center; gap: 10px; }
  .company-mark__dot { width: 22px; height: 22px; border-radius: 50%; background: var(--brand-blue); }
  .company-mark__name { font-weight: 700; font-size: 19px; color: var(--text-main); letter-spacing: 0.5px; }
  .card--front .company-mark { position: absolute; left: 36px; top: 316px; }

  .company-info { position: absolute; left: 36px; top: 364px; color: var(--text-sub); font-size: 10.5px; line-height: 19px; }
  .company-url { position: absolute; right: 36px; top: 384px; color: var(--text-main); font-size: 14px; font-weight: 500; letter-spacing: 0.5px; }

  .card--back .company-mark { position: absolute; left: 0; right: 0; top: 200px; justify-content: center; }
  .card--back .company-mark__dot { background: var(--text-white); }
  .card--back .company-mark__name { color: var(--text-white); font-size: 22px; }
</style>
</head>
<body>
<main class="sheet">
  <section class="card card--front">
    <div class="symbol-area" role="img" aria-label="ブランドシンボルの配置エリア"></div>

    <div class="person">
      <p><span class="person__name">苗字名前</span><span class="person__roman">namae myoji</span></p>
      <p class="person__title">代表取締役</p>
    </div>

    <div class="contact">
      <p class="contact__row">
        <svg class="contact__icon" viewBox="0 0 24 24" aria-hidden="true"><path d="M6.6 10.8a15.1 15.1 0 0 0 6.6 6.6l2.2-2.2a1 1 0 0 1 1-.25 11.4 11.4 0 0 0 3.6.57 1 1 0 0 1 1 1V20a1 1 0 0 1-1 1A17 17 0 0 1 3 4a1 1 0 0 1 1-1h3.5a1 1 0 0 1 1 1c0 1.25.2 2.45.57 3.57a1 1 0 0 1-.25 1z"/></svg>
        <span>000-0000-0000</span>
      </p>
      <p class="contact__row">
        <svg class="contact__icon" viewBox="0 0 24 24" aria-hidden="true"><path d="M3 5h18v14H3z M3 5l9 7 9-7" fill="none" stroke="#2b3f86" stroke-width="2"/></svg>
        <span>aaaaaaaa@aaaaaaa.jp</span>
      </p>
    </div>

    <div class="company-mark">
      <span class="company-mark__dot"></span>
      <span class="company-mark__name">HARUNA SYSTEMS</span>
    </div>

    <div class="company-info">
      <p>〒000-0000 東京都〇〇区〇〇 0-0-0 〇〇〇〇ビル 0F</p>
      <p>Tel. 00-0000-0000　Fax. 00-0000-0000</p>
    </div>
    <p class="company-url">www.haruna-sys.jp</p>
  </section>

  <section class="card card--back">
    <div class="company-mark">
      <span class="company-mark__dot"></span>
      <span class="company-mark__name">HARUNA SYSTEMS</span>
    </div>
  </section>
</main>
</body>
</html>
```